Core Values Poster for Healthcare company

Trying to Create a core values poster for my company. Healthcare Company - We have Neurosurgery, Pain Management, Physical Therapy, Occupational Therapy, Rehab, Imaging, and psychology so far and we are growing fast.

Core Values would Include - (Execution), (Loyalty), (Innovation), (Synergy), (Growth-Oriented), (Ethics & Integrity), (Love), and (Energy)

Please incorporate the Company Logo which is on the website and I have included it in my uploads. As long as the logo stays blue it does not need a gradient effect.

I like the posters made for this contest : https://pinlarkstudio.com.au/flyer-work/briefs/build-team-ideals-flyer-580316

This picture should be memorable so people know our Core Values

Target Market(s)

Staff in the company

Colors

Designer to choose colors to be used in the design.

Requirements
Must have
• Logo
Nice to have
• Pictures for each core value

```html
<!DOCTYPE html>
<html lang="en">
<head>
<meta charset="utf-8">
<title>Lumenta Core Values Poster</title>
<link rel="stylesheet" href="https://fonts.googleapis.com/css2?family=Montserrat:wght@800&family=Old+Standard+TT:wght@400&display=swap">
<style>
  :root {
    --page-bg: #f1f1f1;
    --poster-blue: #29aee9;
    --ink-white: #ffffff;
    --ribbon-dark: #2c2c2c;
    --val-innovation: #ffe46a;
    --val-synergy: #1467c9;
    --val-growth: #4cae4e;
    --val-ethics: #f2693c;
    --val-love: #ee3b37;
    --val-execution: #1d4a97;
    --val-loyalty: #5d2e8e;
    --icon-innovation: #ee4a2a;
    --icon-synergy: #33e0d2;
    --icon-growth: #b8e37c;
    --icon-ethics: #ffd24a;
    --icon-love: #ffd24a;
    --icon-execution: #22c7e0;
    --icon-loyalty: #7fd36a;
  }
  html, body {
    margin: 0;
    width: 1200px;
    height: 1138px;
    overflow: hidden;
    background: var(--page-bg);
  }
  .poster {
    position: absolute;
    left: 211px;
    top: 20px;
    width: 778px;
    height: 1098px;
    display: block;
  }
  .serif { font-family: "Old Standard TT", Georgia, serif; fill: var(--ink-white); }
  .brand-name { font-size: 52px; letter-spacing: 1px; }
  .ribbon-title { font-size: 26px; letter-spacing: 1px; }
  .footer-note { font-size: 19px; }
  .value-label {
    font-family: "Montserrat", Arial, sans-serif;
    font-weight: 800;
    font-size: 16px;
    fill: var(--ink-white);
  }
  .segment { stroke: var(--poster-blue); stroke-width: 12; stroke-linejoin: round; }
</style>
</head>
<body>
<svg class="poster" viewBox="0 0 590 833" xmlns="http://www.w3.org/2000/svg">
  <rect class="poster-field" width="590" height="833" fill="var(--poster-blue)"/>

  <g class="brand">
    <rect class="brand-square" x="125" y="36" width="56" height="56" fill="var(--ink-white)"/>
    <text class="serif brand-name" x="194" y="84">LUMENTA</text>
  </g>

  <g class="ribbon">
    <polygon points="125,134 473,134 461,156 473,178 125,178 137,156" fill="var(--ribbon-dark)"/>
    <text class="serif ribbon-title" x="299" y="165" text-anchor="middle">CORE VALUES</text>
  </g>

  <g class="values-wheel">
    <polygon class="segment" points="290,482 290,242 477.6,332.4" fill="var(--val-innovation)"/>
    <polygon class="segment" points="290,482 477.6,332.4 524,535.4" fill="var(--val-synergy)"/>
    <polygon class="segment" points="290,482 524,535.4 394.1,698.2" fill="var(--val-growth)"/>
    <polygon class="segment" points="290,482 394.1,698.2 185.9,698.2" fill="var(--val-ethics)"/>
    <polygon class="segment" points="290,482 185.9,698.2 56,535.4" fill="var(--val-love)"/>
    <polygon class="segment" points="290,482 56,535.4 102.4,332.4" fill="var(--val-execution)"/>
    <polygon class="segment" points="290,482 102.4,332.4 290,242" fill="var(--val-loyalty)"/>
    <circle cx="290" cy="482" r="18" fill="var(--poster-blue)"/>
  </g>

  <g class="value-icons">
    <circle role="img" aria-label="Lightbulb icon for Innovation" cx="345" cy="345" r="27" fill="var(--icon-innovation)"/>
    <circle role="img" aria-label="Connected team icon for Synergy" cx="420" cy="452" r="27" fill="var(--icon-synergy)"/>
    <circle role="img" aria-label="Seedling in hand icon for Growth-Oriented" cx="398" cy="575" r="27" fill="var(--icon-growth)"/>
    <circle role="img" aria-label="Balance scales icon for Ethics and Integrity" cx="290" cy="632" r="27" fill="var(--icon-ethics)"/>
    <circle role="img" aria-label="Heart in hands icon for Love and Energy" cx="178" cy="575" r="27" fill="var(--icon-love)"/>
    <circle role="img" aria-label="Target icon for Execution" cx="152" cy="452" r="27" fill="var(--icon-execution)"/>
    <circle role="img" aria-label="Lotus in hands icon for Loyalty" cx="232" cy="345" r="27" fill="var(--icon-loyalty)"/>
  </g>

  <g class="value-labels">
    <text class="value-label" text-anchor="middle" transform="translate(197,258) rotate(-25)">Loyalty</text>
    <text class="value-label" text-anchor="middle" transform="translate(402,258) rotate(28)">Innovation</text>
    <text class="value-label" text-anchor="middle" transform="translate(537,418) rotate(78)">Synergy</text>
    <text class="value-label" text-anchor="middle" transform="translate(488,615) rotate(-62)">Growth-Oriented</text>
    <text class="value-label" text-anchor="middle" transform="translate(300,720)">Ethics &amp; Integrity</text>
    <text class="value-label" text-anchor="middle" transform="translate(108,615) rotate(56)">Love, and Energy</text>
    <text class="value-label" text-anchor="middle" transform="translate(58,426) rotate(-80)">Execution</text>
  </g>

  <text class="serif footer-note" x="297" y="789" text-anchor="middle">For more information visit www.lumentacare.com</text>
</svg>
</body>
</html>
```